Business cards

We need business cards for the logo that you designed for our company. Something simple and clean.

Target Market(s)

Homeowners/ people looking for construction work

Industry/Entity Type

Construction

Contact Information for Business Card

Name: Dana Holbrit, Number: 602-547-9164, Email: HolbritBuildingGroup@mailvesta.com ROC# 846203

Font styles to use
Serif

Colors

Designer to choose colors to be used in the design.

Requirements
Must have
• On one side of the card I would like to be all of the personal information I have put above along with the company logo that I have attached.
• On the other side of the card I would like the top half of the card to be the logo and then on the bottom half I would like to have the areas of construction we focus on along with an icon that represents it like the picture I have attached.
• Areas we focus on:
• Roofing, Kitchen and bath Remodel, Water Damage, Storm Damage, Fire Damage, Insurance Specialist
• If we could arrange those in alphabetical order.
Nice to have
• I have added 2 company logos a colorful one and a black one it would be nice to see a couple different options the black logo to be more simple and sleek and the colorful logo to be more colorful

```html
<!DOCTYPE html>
<html lang="en">
<head>
<meta charset="utf-8">
<title>Holbrit Building Group – Business Cards</title>
<link href="https://fonts.googleapis.com/css2?family=Roboto+Condensed:wght@400;700&family=Open+Sans:wght@400;700&display=swap" rel="stylesheet">
<style>
  :root {
    --bg: #2b2b2b;
    --card-black: #0b0b0b;
    --card-white: #ffffff;
    --brand-blue: #3fa9dd;
    --icon-green: #8dc63f;
    --text-light: #f2f2f2;
  }
  html, body {
    margin: 0;
    width: 1200px;
    height: 896px;
    overflow: hidden;
    background: var(--bg);
  }
  .canvas {
    width: 1200px;
    height: 896px;
    display: flex;
    flex-direction: column;
    align-items: center;
    justify-content: center;
    gap: 56px;
  }
  .card {
    position: relative;
    width: 600px;
    height: 343px;
    border-radius: 22px;
    overflow: hidden;
    box-shadow: 0 10px 30px rgba(0,0,0,.45);
  }

  /* Wordmark */
  .wordmark {
    display: flex;
    align-items: center;
    gap: 12px;
    font-family: "Roboto Condensed", sans-serif;
    font-weight: 700;
    color: var(--brand-blue);
    text-transform: uppercase;
    line-height: 1;
  }
  .wordmark-square {
    width: 40px;
    height: 40px;
    background: var(--brand-blue);
    flex: none;
  }
  .wordmark-text { display: flex; flex-direction: column; gap: 4px; }
  .wordmark-name { font-size: 58px; letter-spacing: 3px; }
  .wordmark-sub { font-size: 13px; letter-spacing: 6.5px; }

  /* Services side */
  .card-services { background: var(--card-black); }
  .card-services .wordmark { position: absolute; left: 48px; top: 34px; }
  .service-list {
    position: absolute;
    left: 48px;
    top: 132px;
    margin: 0;
    font-family: "Open Sans", sans-serif;
    font-size: 14px;
    letter-spacing: .6px;
    color: var(--text-light);
    text-transform: uppercase;
    line-height: 1.6;
  }
  .service-icons {
    position: absolute;
    left: 40px;
    right: 40px;
    top: 204px;
    display: flex;
    justify-content: space-between;
  }
  .service {
    width: 96px;
    display: flex;
    flex-direction: column;
    align-items: center;
    font-family: "Open Sans", sans-serif;
    color: var(--text-light);
    text-transform: uppercase;
    text-align: center;
  }
  .service svg { width: 46px; height: 56px; }
  .service-title { font-weight: 700; font-size: 12px; margin-top: 6px; }
  .service-sub { font-size: 9px; letter-spacing: .4px; }
  .service-rule {
    position: absolute;
    left: 236px;
    top: 200px;
    width: 110px;
    height: 2px;
    background: var(--icon-green);
  }

  /* Contact side */
  .card-contact { background: var(--card-white); }
  .card-contact .wave { position: absolute; inset: 0; }
  .card-contact .wordmark { position: absolute; left: 44px; top: 84px; }
  .card-contact .wordmark-name { font-size: 46px; letter-spacing: 2px; }
  .card-contact .wordmark-sub { font-size: 10px; letter-spacing: 5px; }
  .contact {
    position: absolute;
    right: 30px;
    top: 76px;
    text-align: right;
    font-family: "Open Sans", sans-serif;
    color: var(--text-light);
  }
  .contact-name {
    font-family: "Roboto Condensed", sans-serif;
    font-size: 28px;
    color: var(--brand-blue);
    text-transform: uppercase;
    margin: 0;
    line-height: 1.1;
  }
  .contact-role { font-size: 13px; margin: 2px 0 16px; }
  .contact-line {
    display: flex;
    justify-content: flex-end;
    align-items: center;
    gap: 8px;
    font-size: 13px;
    line-height: 1.8;
  }
  .contact-line svg { width: 11px; height: 11px; flex: none; }
  .contact-line .accent { color: var(--brand-blue); }
  .licence {
    position: absolute;
    left: 34px;
    bottom: 16px;
    margin: 0;
    font-family: "Open Sans", sans-serif;
    font-size: 15px;
    color: var(--text-light);
  }
  .licence span { color: var(--brand-blue); }
</style>
</head>
<body>
<main class="canvas">

  <section class="card card-services" aria-label="Services side">
    <div class="wordmark">
      <span class="wordmark-square"></span>
      <span class="wordmark-text">
        <span class="wordmark-name">Holbrit</span>
        <span class="wordmark-sub">Building Group</span>
      </span>
    </div>
    <p class="service-list">
      Roofing - Kitchen and Bath Remodel - Water Damage<br>
      Storm Damage - Fire Damage - Insurance Specialist
    </p>
    <span class="service-rule"></span>
    <div class="service-icons">
      <div class="service">
        <svg viewBox="0 0 46 56"><path d="M23 55 L8 38 A21 21 0 1 1 38 38 Z" fill="var(--icon-green)"/><circle cx="23" cy="23" r="15" fill="#fff"/><path d="M23 13 C18 20 16 24 16 27 a7 7 0 0 0 14 0 C30 24 28 20 23 13Z" fill="#2f7fc1"/></svg>
        <span class="service-title">Water</span><span class="service-sub">Damage</span>
      </div>
      <div class="service">
        <svg viewBox="0 0 46 56"><path d="M23 55 L8 38 A21 21 0 1 1 38 38 Z" fill="var(--icon-green)"/><circle cx="23" cy="23" r="15" fill="#fff"/><path d="M24 12 C27 19 31 21 30 28 a7 7 0 0 1 -14 0 C16 23 20 22 21 17 C23 21 25 20 24 12Z" fill="#d9472b"/></svg>
        <span class="service-title">Fire</span><span class="service-sub">Damage</span>
      </div>
      <div class="service">
        <svg viewBox="0 0 46 56"><path d="M23 55 L8 38 A21 21 0 1 1 38 38 Z" fill="var(--icon-green)"/><circle cx="23" cy="23" r="15" fill="#fff"/><g fill="#4d8a2a"><circle cx="18" cy="19" r="3"/><circle cx="25" cy="18" r="3"/><circle cx="29" cy="24" r="3"/><circle cx="21" cy="26" r="3"/><circle cx="16" cy="27" r="2"/></g></svg>
        <span class="service-title">Mold</span><span class="service-sub">Remediation</span>
      </div>
      <div class="service">
        <svg viewBox="0 0 46 56"><path d="M23 55 L8 38 A21 21 0 1 1 38 38 Z" fill="var(--icon-green)"/><circle cx="23" cy="23" r="15" fill="#fff"/><path d="M15 26 a5 5 0 0 1 3 -9 a7 7 0 0 1 13 2 a4 4 0 0 1 0 8 Z" fill="#2f5fa8"/><path d="M23 27 l-3 6 h3 l-2 5 5 -7 h-3 l2 -4Z" fill="#f0b323"/></svg>
        <span class="service-title">Storm</span><span class="service-sub">Damage</span>
      </div>
      <div class="service">
        <svg viewBox="0 0 46 56"><path d="M23 55 L8 38 A21 21 0 1 1 38 38 Z" fill="var(--icon-green)"/><circle cx="23" cy="23" r="15" fill="#f39a3a"/><rect x="15" y="15" width="16" height="16" fill="#fff"/><g fill="#f39a3a"><rect x="18" y="18" width="3" height="3"/><rect x="25" y="18" width="3" height="3"/><rect x="18" y="24" width="3" height="3"/><rect x="25" y="24" width="3" height="3"/></g></svg>
        <span class="service-title">Commercial</span><span class="service-sub">Services</span>
      </div>
    </div>
  </section>

  <section class="card card-contact" aria-label="Contact side">
    <svg class="wave" viewBox="0 0 600 343" preserveAspectRatio="none">
      <path d="M430 0 C350 40 330 120 280 190 C230 255 120 275 0 285 L0 343 L600 343 L600 0 Z" fill="var(--card-black)"/>
      <path d="M416 0 C336 40 316 120 266 186 C216 250 110 268 0 276" fill="none" stroke="var(--brand-blue)" stroke-width="6"/>
    </svg>
    <div class="wordmark">
      <span class="wordmark-square"></span>
      <span class="wordmark-text">
        <span class="wordmark-name">Holbrit</span>
        <span class="wordmark-sub">Building Group</span>
      </span>
    </div>
    <div class="contact">
      <p class="contact-name">Dana Holbrit</p>
      <p class="contact-role">Director</p>
      <div class="contact-line"><span>602-547-9164</span>
        <svg viewBox="0 0 12 12"><path d="M2 1 h3 l1 3 -2 1 a7 7 0 0 0 3 3 l1 -2 3 1 v3 a1 1 0 0 1 -1 1 A10 10 0 0 1 1 2 a1 1 0 0 1 1 -1Z" fill="var(--brand-blue)"/></svg>
      </div>
      <div class="contact-line"><span>HolbritBuildingGroup@mailvesta.com</span>
        <svg viewBox="0 0 12 12"><rect x="1" y="2.5" width="10" height="7" fill="none" stroke="var(--brand-blue)" stroke-width="1.3"/><path d="M1 3 L6 7 L11 3" fill="none" stroke="var(--brand-blue)" stroke-width="1.3"/></svg>
      </div>
      <div class="contact-line"><span>www.<span class="accent">HolbritGroup</span>.com</span>
        <svg viewBox="0 0 12 12"><circle cx="6" cy="6" r="5" fill="var(--brand-blue)"/><path d="M1 6 h10 M6 1 v10" stroke="var(--card-black)" stroke-width=".8"/></svg>
      </div>
    </div>
    <p class="licence"><span>ROC#</span> 846203</p>
  </section>

</main>
</body>
</html>
```